Larchmere Hockey Academy

We are are Ice Hockey Development Company that provided on-ice Hockey development services. We need a Landing Page with tabs to direct to individual program pages.
Landing Page
About Page
Winter Program Page
Spring Program Page
Summer Program Page
Team Page
Tournament Page

```html
<!DOCTYPE html>
<html lang="en">
<head>
<meta charset="utf-8">
<title>Larchmere Hockey Academy</title>
<link rel="stylesheet" href="https://fonts.googleapis.com/css2?family=Poppins:wght@400;500;600;700;800&display=swap">
<style>
:root{
  --green:#1f8a1f;
  --green-soft:#3fa043;
  --green-dark:#0f6b16;
  --ink:#222222;
  --text:#3a3a3a;
  --rule:#e3e3e3;
  --panel:#f0f0f0;
  --footer:#000000;
  --white:#ffffff;
}
*{box-sizing:border-box;margin:0;padding:0}
html,body{width:1200px;height:3804px;overflow:hidden;background:var(--white)}
body{font-family:'Poppins',sans-serif;color:var(--text);position:relative}
.abs{position:absolute}
.btn{position:absolute;display:flex;align-items:center;justify-content:center;background:var(--green);color:var(--white);font-weight:600;font-size:14px;letter-spacing:.3px;text-transform:uppercase}
.photo{position:absolute}

/* header */
.site-header{position:absolute;left:0;top:0;width:1200px;height:118px}
.brand{position:absolute;left:74px;top:36px;display:flex;align-items:center;gap:8px}
.brand-mark{width:14px;height:14px;background:var(--green)}
.brand-name{font-weight:800;font-size:21px;line-height:22px;color:var(--ink);letter-spacing:.5px;text-transform:uppercase}
.main-nav{position:absolute;right:74px;top:58px;display:flex;gap:33px;font-size:13px;font-weight:700;color:var(--ink);text-transform:uppercase}
.main-nav .active{color:var(--green)}

/* hero */
.hero{position:absolute;left:0;top:118px;width:1200px;height:692px;background:radial-gradient(ellipse at 50% 35%,#5f7ea3 0%,#2e4565 45%,#1c2b43 70%),#26364f}
.hero-floor{position:absolute;left:0;bottom:0;width:1200px;height:260px;background:linear-gradient(180deg,#7d93ad,#b9c6d4)}
.hero-title{position:absolute;left:0;width:1200px;top:228px;text-align:center;font-weight:800;font-size:68px;color:var(--white);letter-spacing:1px}
.hero-sub{position:absolute;left:0;width:1200px;top:307px;text-align:center;font-size:27px;line-height:30px;color:var(--white);font-weight:500}

/* about */
.about-image{left:74px;top:889px;width:512px;height:426px;background:linear-gradient(135deg,#aab6c4,#d4443f 45%,#e7e9ec 70%,#9aa5b1)}
.about-title{left:616px;top:898px;font-size:32px;font-weight:700;color:var(--ink)}
.about-text{left:616px;top:950px;width:500px;font-size:15px;line-height:29.5px;color:#444}
.about-text p+p{margin-top:8px}
.divider{left:74px;top:1404px;width:1052px;height:1px;background:var(--rule)}

/* programs */
.programs-bg{left:0;top:1411px}
.program-card{position:absolute;top:1560px;width:328px;height:394px;overflow:hidden}
.program-card svg{position:absolute;left:0;top:0}
.program-label{position:absolute;left:25px;top:340px;color:var(--white);font-weight:700;font-size:24px;text-transform:uppercase;letter-spacing:.5px}

/* team */
.team-photo{width:242px;height:241px}
.team-name{position:absolute;width:242px;text-align:center;font-weight:700;font-size:16px;color:var(--green-dark);text-transform:uppercase}
.team-title{right:74px;top:2253px;font-size:32px;font-weight:700;color:var(--ink)}
.team-text{right:74px;top:2307px;width:290px;text-align:right;font-size:15px;line-height:29.5px;color:#444}

/* tournament */
.tournament{left:0;top:2812px;width:1200px;height:568px;background:var(--panel)}
.tournament-title{left:74px;top:2880px;font-size:32px;font-weight:700;color:var(--ink)}
.event-card{position:absolute;top:2959px;width:242px;height:336px;background:var(--white)}
.event-image{width:242px;height:184px}
.event-date{position:absolute;left:16px;top:205px;font-size:14px;font-weight:500;color:var(--ink)}
.event-name{position:absolute;left:16px;top:231px;font-size:18px;font-weight:600;color:var(--green)}
.event-text{position:absolute;left:16px;top:264px;width:215px;font-size:15px;line-height:26px;color:var(--ink)}

/* newsletter */
.newsletter-title{left:316px;top:3426px;font-size:32px;font-weight:700;color:var(--ink)}
.newsletter-text{left:316px;top:3474px;width:330px;font-size:15px;line-height:25px;color:#444}
.signup{left:675px;top:3441px;width:451px;height:74px;border:1px solid #d4d4d4}
.signup-field{position:absolute;left:16px;top:26px;font-size:15px;color:#444}
.signup-btn{left:290px;top:6px;width:154px;height:60px;background:var(--green-dark);font-size:16px;font-weight:700}

/* footer */
.site-footer{left:0;top:3572px;width:1200px;height:232px;background:var(--footer)}
.footer-nav{position:absolute;left:0;width:1200px;top:72px;display:flex;justify-content:center;gap:33px;color:var(--white);font-size:14px;font-weight:700;text-transform:uppercase}
.copyright{position:absolute;left:0;width:1200px;top:115px;text-align:center;color:#ddd;font-size:14px}
.socials{position:absolute;left:500px;top:152px;display:flex;gap:21px}
.socials span{width:22px;height:22px;border-radius:50%;background:var(--white);display:block}
</style>
</head>
<body>

<header class="site-header">
  <div class="brand"><span class="brand-mark"></span><span class="brand-name">Larchmere<br>Hockey</span></div>
  <nav class="main-nav">
    <span class="active">Home</span><span>About</span><span>Winter Program</span><span>Spring Program</span><span>Summer Program</span><span>Team</span><span>Tournament</span>
  </nav>
</header>

<section class="hero" role="img" aria-label="Two ice hockey players facing off at centre ice in a lit arena">
  <div class="hero-floor"></div>
  <h1 class="hero-title">LARCHMERE HOCKEY</h1>
  <p class="hero-sub">We are an Ice Hockey Development Company that provides<br>on-ice Hockey development services.</p>
  <span class="btn" style="left:517px;top:398px;width:166px;height:54px">Read More</span>
</section>

<section class="about">
  <div class="photo about-image" role="img" aria-label="Two young players battling for the puck on the ice"></div>
  <h2 class="abs about-title">ABOUT LARCHMERE HOCKEY</h2>
  <div class="abs about-text">
    <p>Sed ut perspiciatis unde omnis iste natus error sit voluptatem accusantium doloremque lau dantium magni dolores eos qui ratione voluptatem sequi nesciunt.</p>
    <p>Neque porro quisquam est, qui dolorem ipsum quia dolor sit amet, consectetur, adipisci velit, sed quia non numquam eius modi tempora incidunt ut labore et dolore magnam aliquam quaerat voluptatem. Ut enim ad minima veniam, quis nostrum exercitationem ullam corporis suscipit laboriosam, nisi ut aliquid ex ea commodi consequatur.</p>
  </div>
  <span class="btn" style="left:616px;top:1244px;width:165px;height:55px">Read More</span>
  <div class="abs divider"></div>
</section>

<section class="programs">
  <svg class="abs programs-bg" width="1200" height="616" viewBox="0 0 1200 616" role="img" aria-label="Ice rink surface backdrop">
    <defs><linearGradient id="rink" x1="0" y1="0" x2="1" y2="1"><stop offset="0" stop-color="#13263b"/><stop offset=".5" stop-color="#4b6378"/><stop offset="1" stop-color="#8ea1b2"/></linearGradient></defs>
    <polygon points="0,0 1200,494 1200,616 0,616" fill="url(#rink)"/>
  </svg>
  <div class="program-card" style="left:74px">
    <svg width="328" height="394" role="img" aria-label="Players skating in a winter game"><rect width="328" height="394" fill="#d9dde2"/><rect y="150" width="328" height="160" fill="#c04a40" opacity=".35"/><polygon points="0,282 328,330 328,394 0,394" fill="var(--green-soft)" opacity=".95"/></svg>
    <span class="program-label">Winter Program</span>
  </div>
  <div class="program-card" style="left:437px">
    <svg width="328" height="394" role="img" aria-label="Player in dark kit skating under arena lights"><rect width="328" height="394" fill="#2f3f5a"/><rect y="220" width="328" height="174" fill="#8e9db0"/><polygon points="0,282 328,330 328,394 0,394" fill="var(--green-soft)" opacity=".95"/></svg>
    <span class="program-label">Spring Program</span>
  </div>
  <div class="program-card" style="left:798px">
    <svg width="328" height="394" role="img" aria-label="Player skating on an outdoor rink"><rect width="328" height="394" fill="#e9e9e9"/><rect x="40" y="60" width="120" height="200" fill="#c8443e" opacity=".35"/><polygon points="0,282 328,330 328,394 0,394" fill="var(--green-soft)" opacity=".95"/></svg>
    <span class="program-label">Summer Program</span>
  </div>
</section>

<section class="team">
  <div class="photo team-photo" style="left:74px;top:2103px;background:linear-gradient(160deg,#3a5a88,#d8553e 55%,#cdd6e0)" role="img" aria-label="Team member in orange kit"></div>
  <span class="team-name" style="left:74px;top:2354px">Name Heading</span>
  <div class="photo team-photo" style="left:74px;top:2397px;background:linear-gradient(160deg,#2e4565,#aab9c9 60%,#dfe5ec)" role="img" aria-label="Team member in white jersey"></div>
  <span class="team-name" style="left:74px;top:2648px">Name Heading</span>
  <div class="photo team-photo" style="left:330px;top:2164px;background:linear-gradient(170deg,#e7ecf1,#c9a93a 55%,#a9b7c4)" role="img" aria-label="Two players contesting the puck"></div>
  <span class="team-name" style="left:330px;top:2415px">Name Heading</span>
  <div class="photo team-photo" style="left:330px;top:2458px;background:linear-gradient(170deg,#f1f1f1,#3a9a4a 50%,#e3e3e3)" role="img" aria-label="Young player in green jersey"></div>
  <span class="team-name" style="left:330px;top:2709px">Name Heading</span>
  <div class="photo" style="left:587px;top:2239px;width:242px;height:325px;background:linear-gradient(170deg,#1b2638,#d23a34 50%,#2b3548)" role="img" aria-label="Team captain in red jersey"></div>
  <span class="team-name" style="left:587px;top:2573px">Name Heading</span>
  <h2 class="abs team-title">OUR TEAM</h2>
  <p class="abs team-text">Sed ut perspiciatis unde omnis iste natus error sit voluptatem accusantium doloremque lau dantium magni dolores eos qui ratione voluptatem sequi nesciunt.</p>
  <span class="btn" style="left:960px;top:2512px;width:166px;height:53px">View All Team</span>
</section>

<section class="abs tournament"></section>
<h2 class="abs tournament-title">TOURNAMENT</h2>
<svg class="abs" style="left:1048px;top:2886px" width="78" height="30" viewBox="0 0 78 30" aria-label="Previous and next">
  <circle cx="15" cy="15" r="15" fill="#333"/><path d="M22 15H9M14 9l-6 6 6 6" stroke="#fff" stroke-width="3" fill="none"/>
  <circle cx="63" cy="15" r="15" fill="var(--green)"/><path d="M56 15h13M64 9l6 6-6 6" stroke="#fff" stroke-width="3" fill="none"/>
</svg>
<article class="event-card" style="left:74px"><div class="event-image" style="background:linear-gradient(180deg,#101a2a,#2f6fb0 60%,#9fb5c9)" role="img" aria-label="Team in blue kit lined up on the ice"></div><span class="event-date">MAR28, 2023</span><h3 class="event-name">NEMO ENIM IPSAM</h3><p class="event-text">Neque porro quisquam est, qui dolorem ipsum.</p></article>
<article class="event-card" style="left:345px"><div class="event-image" style="background:linear-gradient(180deg,#0d1522,#3a4a60 60%,#8fa2b6)" role="img" aria-label="Two players chasing the puck"></div><span class="event-date">MAR28, 2023</span><h3 class="event-name">NEMO ENIM IPSAM</h3><p class="event-text">Neque porro quisquam est, qui dolorem ipsum.</p></article>
<article class="event-card" style="left:615px"><div class="event-image" style="background:linear-gradient(180deg,#1a2332,#c23a36 55%,#a7b4c1)" role="img" aria-label="Team in red kit skating forward"></div><span class="event-date">MAR28, 2023</span><h3 class="event-name">NEMO ENIM IPSAM</h3><p class="event-text">Neque porro quisquam est, qui dolorem ipsum.</p></article>
<article class="event-card" style="left:886px"><div class="event-image" style="background:linear-gradient(180deg,#3b4f6b,#8fc3df 55%,#d6dee6)" role="img" aria-label="Player in light blue kit on the ice"></div><span class="event-date">MAR28, 2023</span><h3 class="event-name">NEMO ENIM IPSAM</h3><p class="event-text">Neque porro quisquam est, qui dolorem ipsum.</p></article>

<section class="newsletter">
  <div class="brand" style="top:3440px"><span class="brand-mark"></span><span class="brand-name">Larchmere<br>Hockey</span></div>
  <h2 class="abs newsletter-title">NEWSLETTER</h2>
  <p class="abs newsletter-text">Sed ut perspiciatis unde omnis iste natus error sit voluptatem accusantium.</p>
  <div class="abs signup"><span class="signup-field">Email Address</span><span class="btn signup-btn">Subscribe</span></div>
</section>

<footer class="abs site-footer">
  <nav class="footer-nav"><span>Home</span><span>About</span><span>Winter Program</span><span>Spring Program</span><span>Summer Program</span><span>Team</span><span>Tournament</span></nav>
  <p class="copyright">© 2023 Larchmere Hockey All Rights Reserved.</p>
  <div class="socials"><span aria-label="Social link"></span><span aria-label="Social link"></span><span aria-label="Social link"></span><span aria-label="Social link"></span><span aria-label="Social link"></span></div>
</footer>

</body>
</html>
```